Review Site Redesign

We have a rather ambitious goal to reinvent (redesign) the way bank financial review sites present information. In that respect, we’re looking for an innovative creative design.
As examples of what I would call bad or boring design please look at the following sites:
1. http://brisklend.example/se
2. http://vantorquay.example/se/privatlan
3. http://glimsworth.example/no
These are the traditional way these types of review sites are organized: dull and boring. I think we can do a lot better than that.
I need a site that will capture attention end engage the visitor; a site that will create a more interactive and less passive user experience.
Scope of work should also include logo font and additional content space for articles, FAQ, widgets, social media links, etc.

Not sure what to advise you as best format - maybe a flash or js carousel, gallery, wheel, logo image matrix, or something else.
Maybe some kind of interactive logo matrix such as this site: http://www.quarnibo.example/
Please apply your best creative mind work to this problem.
Also, please think about creative use of background images, stock photos, etc.
For logo font use can use URL “pellrowatt.example” as placeholder.

```html
<!DOCTYPE html>
<html lang="en">
<head>
<meta charset="utf-8">
<title>Pellrowatt.example – Finance Reviews</title>
<link href="https://fonts.googleapis.com/css2?family=Arimo:wght@400;700&family=Lora:ital@1&display=swap" rel="stylesheet">
<style>
:root{
  --red:#e8362b;
  --red-dark:#c92a20;
  --ink:#2b2b2b;
  --text:#3c3c3c;
  --muted:#8a8a8a;
  --line:#dcdcdc;
  --panel:#f1f1f1;
  --green:#3f9e1c;
  --green-dark:#2f7f12;
  --white:#ffffff;
}
*{box-sizing:border-box;margin:0;padding:0}
html,body{width:1200px;height:1186px;overflow:hidden}
body{font-family:"Arimo",Arial,sans-serif;color:var(--text);background:#e9e9e9;position:relative}
.backdrop{position:absolute;inset:0;background:linear-gradient(90deg,#7d7d7d 0,#c9c9c9 8%,#eeeeee 20%,#eeeeee 80%,#c4c4c4 92%,#777 100%);}
.backdrop::after{content:"";position:absolute;left:0;right:0;top:760px;bottom:0;background:linear-gradient(#ffffff00,#fafafa 140px)}
.page{position:absolute;left:115px;top:0;width:970px;height:955px;background:#f6f6f6;box-shadow:0 0 14px rgba(0,0,0,.35)}
.abs{position:absolute}
/* header */
.logo{left:39px;top:36px;font-size:34px;color:#333;letter-spacing:-.5px}
.contact{left:425px;top:36px;display:flex;align-items:center;gap:12px}
.phone-ring{width:30px;height:30px;border-radius:50%;border:2px solid var(--red);display:flex;align-items:center;justify-content:center}
.contact small{display:block;color:var(--red);font-size:11px}
.contact strong{font-size:19px;color:#222}
.search{left:732px;top:37px;width:196px;height:28px;background:var(--white);border:1px solid #ddd;font-size:11px;color:#999;padding:7px 12px;display:flex;justify-content:space-between}
/* nav */
.mainnav{left:17px;top:105px;width:953px;height:39px;background:var(--red);display:flex;align-items:center}
.mainnav a{color:#fff;text-decoration:none;font-size:14px;padding:0 22px;height:39px;line-height:39px}
.mainnav a.current{background:var(--ink);margin-left:6px;padding:0 24px}
.subnav{left:17px;top:144px;width:953px;height:24px;background:#2a2a2a;display:flex;align-items:center;font-size:11px;color:#cfcfcf}
.subnav span{padding:0 12px}
.social{margin-left:auto;display:flex;gap:8px;align-items:center;padding-right:14px;font-style:italic;color:#eee}
.social i{width:10px;height:10px;background:#ddd;border-radius:2px;display:inline-block}
/* hero */
.hero{left:17px;top:180px;width:934px;height:329px;background:linear-gradient(90deg,#e8e8e8 0,#e3e3e3 38%,#b9b2a8 55%,#6e6f73 78%,#cfd0cf 100%)}
.hero-title{left:58px;top:51px;font-size:27px;font-weight:700;color:#222;line-height:34px}
.loanbox{left:58px;top:128px;width:335px;height:163px;background:rgba(255,255,255,.92);border:1px solid #ddd;padding:18px 26px}
.loanbox h3{color:var(--red);font-weight:400;font-size:16px;margin-bottom:12px}
.loanbox ul{list-style:none;display:grid;grid-template-columns:1fr 1fr;row-gap:12px;font-size:11.5px;color:#444}
.loanbox li{display:flex;gap:8px;align-items:center}
.tick{width:10px;height:10px;border-radius:50%;background:#4aa12a}
.btn-green{display:inline-flex;align-items:center;gap:14px;background:linear-gradient(#4db126,var(--green-dark));color:#fff;font-weight:700;font-size:15px;padding:9px 20px;border-radius:2px}
.loanbox .btn-green{margin-top:16px}
.dots{right:16px;bottom:14px;display:flex;gap:5px}
.dots i{width:11px;height:11px;border-radius:50%;background:#fff;opacity:.8}
.dots i:first-child{background:#555;border:2px solid #fff}
/* section bar */
.section-pill{left:22px;top:537px;height:49px;width:262px;background:var(--red);color:#fff;font-weight:700;font-size:15px;display:flex;align-items:center;padding-left:18px;gap:14px;border-radius:25px 0 0 25px;clip-path:polygon(0 0,94% 0,100% 50%,94% 100%,0 100%)}
.section-pill .badge{width:40px;height:40px;border-radius:50%;background:#fff;display:flex;align-items:center;justify-content:center;margin-left:-13px}
.divider{left:290px;top:561px;width:250px;border-top:1px solid #ccc}
.view-label{right:130px;top:547px;font-family:"Lora",Georgia,serif;font-style:italic;color:#aaa;font-size:16px;white-space:nowrap}
.view-btn{left:852px;top:540px;width:101px;height:34px;background:var(--ink);color:#fff;font-size:15px;display:flex;align-items:center;justify-content:center}
/* bank cards */
.bank-card{top:612px;width:163px;height:91px;background:var(--white);border:1px solid #e1e1e1;display:flex;align-items:center;justify-content:center;gap:9px;font-size:16px;font-weight:700;color:#1f3d7a;white-space:nowrap}
.bank-card i{width:20px;height:20px;border-radius:50%;background:#1f3d7a;flex:none}
/* table */
.compare{left:19px;top:723px;width:932px;border-collapse:collapse;background:var(--white);font-size:13px}
.compare th{height:45px;background:linear-gradient(#fafafa,#ececec);font-weight:400;color:#444;border:1px solid var(--line)}
.compare td{border:1px solid var(--line);text-align:center;vertical-align:middle;height:107px}
.supplier{display:flex;flex-direction:column;align-items:center;gap:18px}
.supplier .name{display:flex;gap:8px;align-items:center;font-size:19px;font-weight:700;color:#1f3d7a}
.supplier .name i{width:24px;height:24px;border-radius:50%;background:#1f3d7a}
.ribbon{border:1px solid #ddd;background:#fafafa;color:var(--red);font-size:13px;padding:4px 12px}
.stars{color:#e8a200;letter-spacing:1px;margin-top:6px;font-size:13px}
.stars span{color:#888}
.amount{color:#555;line-height:20px}
.amount em{color:var(--red);font-style:normal;display:block}
.reqs{color:#777;font-size:12px;line-height:19px;padding:0 10px}
.btn-red{background:linear-gradient(#f04a3d,var(--red-dark));color:#fff;font-size:11px;padding:9px 10px;display:inline-block;border-radius:2px}
.compare .note td{height:25px;font-size:11px;color:#777;text-align:left;padding-left:12px;background:#f5f5f5}
/* footer */
.foot-h{font-size:14px;color:#333;display:flex;gap:8px;align-items:center}
.foot-h::after{content:"";position:absolute;top:24px;left:0;width:100%;border-top:1px dashed #e88}
.about{left:134px;top:976px;width:378px}
.about p{margin-top:30px;font-size:11px;line-height:14px;color:#333}
.btn-more{margin-top:14px;display:inline-block;background:var(--red);color:#fff;font-size:11px;padding:5px 13px}
.about hr{border:0;border-top:1px solid #ddd;margin-top:8px}
.sitemap{left:557px;top:976px;width:262px}
.sitemap ul{margin-top:30px;list-style:none;columns:2;font-size:11px;color:#444;line-height:19px}
.sitemap li::before{content:"";display:inline-block;width:6px;height:6px;border-radius:50%;border:1px solid #888;margin-right:8px}
.sitemap li.on{background:var(--red);color:#fff;display:inline-block;padding:0 6px;line-height:16px}
.sitemap li.on::before{border-color:#fff}
.map{left:869px;top:977px;width:196px;height:94px;background:linear-gradient(135deg,#ececec,#d9d9d9);border:2px solid #fff;box-shadow:0 0 2px #aaa}
.foot-contact{left:869px;top:1084px;display:flex;align-items:center;gap:14px}
.foot-contact small{display:block;font-size:11px;color:#777}
.foot-contact strong{font-size:19px;color:var(--red)}
.copyright{left:134px;top:1148px;font-size:11px;color:#555}
</style>
</head>
<body>
<div class="backdrop" role="img" aria-label="Blurred office photograph background"></div>

<div class="page">
  <div class="abs logo">Pellrowatt.example</div>
  <div class="abs contact">
    <div class="phone-ring"><svg width="14" height="14" viewBox="0 0 24 24"><path d="M6.6 10.8a15 15 0 0 0 6.6 6.6l2.2-2.2a1 1 0 0 1 1-.25 11 11 0 0 0 3.6.6 1 1 0 0 1 1 1V20a1 1 0 0 1-1 1A17 17 0 0 1 3 4a1 1 0 0 1 1-1h3.5a1 1 0 0 1 1 1 11 11 0 0 0 .6 3.6 1 1 0 0 1-.25 1z" fill="#333"/></svg></div>
    <div><small>Contact Now</small><strong>1800 0000 246</strong></div>
  </div>
  <div class="abs search"><span>Search</span><svg width="12" height="12" viewBox="0 0 12 12"><circle cx="5" cy="5" r="3.5" fill="none" stroke="#aaa" stroke-width="1.5"/><path d="M8 8l3 3" stroke="#aaa" stroke-width="1.5"/></svg></div>

  <nav class="abs mainnav">
    <a class="current">Home</a><a>All About Finances</a><a>Finance Dictionary</a><a>Safety</a><a>About Us</a><a>Plug</a><a>Forum</a><a>Contact Us</a>
  </nav>
  <div class="abs subnav">
    <span>All loans</span><span>Small loans</span><span>Large loans</span><span>Consumer</span><span>Credit</span><span>Favorite Track</span><span>News</span>
    <div class="social">Connect With Us <i></i><i></i><i></i><i></i><i></i></div>
  </div>

  <section class="abs hero" role="img" aria-label="Photo of two business people reviewing loan documents at a desk">
    <h1 class="abs hero-title">We Could Help Make Your<br>Finances Work Harder</h1>
    <div class="abs loanbox">
      <h3>★ Choose Your Loan Here</h3>
      <ul>
        <li><i class="tick"></i>Consumer Lending</li><li><i class="tick"></i>Unsecured Loans</li>
        <li><i class="tick"></i>Car Loans</li><li><i class="tick"></i>Consumer loans</li>
      </ul>
      <span class="btn-green">Apply Now <span>›</span></span>
    </div>
    <div class="abs dots"><i></i><i></i><i></i><i></i></div>
  </section>

  <div class="abs section-pill"><span class="badge"><svg width="18" height="18" viewBox="0 0 20 20"><circle cx="10" cy="6" r="4" fill="#e8362b"/><path d="M2 19a8 7 0 0 1 16 0z" fill="#e8362b"/></svg></span>Consumer Lending</div>
  <div class="abs divider"></div>
  <div class="abs view-label">View all Consumers</div>
  <div class="abs view-btn">View all</div>

  <div class="abs bank-card" style="left:19px"><i></i>Kestrel</div>
  <div class="abs bank-card" style="left:211px"><i></i>Orvane</div>
  <div class="abs bank-card" style="left:404px"><i></i>Halbrook Bank</div>
  <div class="abs bank-card" style="left:596px"><i></i>Meadowline</div>
  <div class="abs bank-card" style="left:790px"><i></i>Tessaport</div>

  <table class="abs compare">
    <thead><tr><th style="width:216px">Supplier</th><th style="width:135px">Type</th><th style="width:132px">Amount</th><th style="width:163px">Requirements</th><th style="width:110px">More</th><th>Apply Now</th></tr></thead>
    <tbody>
      <tr>
        <td rowspan="2"><div class="supplier"><div class="name"><i></i>Kestrel</div><div class="ribbon">Kestrel National Bank</div></div></td>
        <td>Consumer Loans<div class="stars">★★★<span>★★</span></div></td>
        <td class="amount">20,000<em>to</em>350,000</td>
        <td class="reqs">Anual income less than 20,000 $. Age of 20. No betalningsanm.</td>
        <td><span class="btn-red">Read more</span></td>
        <td><span class="btn-green">Apply Now <span>›</span></span></td>
      </tr>
      <tr class="note"><td colspan="5">Lendwick the loan broker online that offer quick and easy loan of up to £ 15,000</td></tr>
    </tbody>
  </table>
</div>

<div class="abs about">
  <div class="foot-h" style="position:relative"><svg width="8" height="14" viewBox="0 0 8 14"><circle cx="4" cy="2.5" r="2.5" fill="#333"/><rect x="1" y="6" width="6" height="8" fill="#333"/></svg>About Company</div>
  <p>Lorem Ipsum is simply dummy text of the printing and typesetting industry. Lorem Ipsum has been the industry's standard dummy text ever since the 1500s, when an unknown printer took a galley of type and scrambled it to make a type specimen book. It has survived not only five centuries, but also the leap into electronic typesetting, remaining essentially unchanged.</p>
  <span class="btn-more">Learn more</span>
  <hr>
</div>

<div class="abs sitemap">
  <div class="foot-h" style="position:relative"><svg width="14" height="12" viewBox="0 0 14 12"><path d="M7 0l7 6h-2v6H2V6H0z" fill="#333"/></svg>Site Map</div>
  <ul>
    <li>Home</li><li class="on">All About Finances</li><li>Finance Dictionary</li><li>Safety</li><li>Information</li><li>Calculate Loan</li>
    <li>About Us</li><li>Consumer Lending</li><li>Plug</li><li>Forum</li><li>Articals</li><li>Contact Us</li>
  </ul>
</div>

<div class="abs map" role="img" aria-label="Street map showing office location"><svg style="position:absolute;left:88px;top:28px" width="16" height="22" viewBox="0 0 16 22"><path d="M8 0a8 8 0 0 1 8 8c0 6-8 14-8 14S0 14 0 8a8 8 0 0 1 8-8z" fill="#e8362b"/><circle cx="8" cy="8" r="3" fill="#fff"/></svg></div>
<div class="abs foot-contact">
  <div class="phone-ring"><svg width="14" height="14" viewBox="0 0 24 24"><path d="M6.6 10.8a15 15 0 0 0 6.6 6.6l2.2-2.2a1 1 0 0 1 1-.25 11 11 0 0 0 3.6.6 1 1 0 0 1 1 1V20a1 1 0 0 1-1 1A17 17 0 0 1 3 4a1 1 0 0 1 1-1h3.5a1 1 0 0 1 1 1 11 11 0 0 0 .6 3.6 1 1 0 0 1-.25 1z" fill="#333"/></svg></div>
  <div><small>Contact Now</small><strong>1800 0000 246</strong></div>
</div>
<div class="abs copyright">Copyrights © 2012 Pellrowatt.example</div>
</body>
</html>
```